Create a "germ free" Poster Design Project

Hi we're a media business who sells advertising space on a unique dispensing device that also sanitizes your hands.

I'm looking for a poster design that highlights the need to sanitize hands which removes 99.9% of germs and also promotes a healthy & clean lifestyle.
(you may want to use kid friendly images of bugs to highlight germs)
Whilst the primary message will be to sanitize your hands the secondary message is also to "use this space" to advertise on.

The poster should be colorful yet simple and not too wordy.

Thanks

Target Market(s)

General cunsumer public but more specifically women and moms

Industry/Entity Type

Advertising

Requirements
Must have
• A central picture (animated or real) to highlight the practice of sanitizing hands (or removing germs)
Perhaps an arrow down to invite consumers to "try it now, its free'
Nice to have
• Referal to our web site: Brelvona.com.au (currently not operational) and email info@brelvona.com.au
Perhaps an image of a baby's hand with a creative tag line.
Should not have
• Nothing too gross looking

```html
<!DOCTYPE html>
<html lang="en">
<head>
<meta charset="utf-8">
<title>Germ Free Poster – Brelvona</title>
<link rel="stylesheet" href="https://fonts.googleapis.com/css2?family=Ubuntu:wght@400;500;700&display=swap">
<style>
  :root {
    --stage: #e4e4e4;
    --paper: #f6f5f2;
    --band: #ebe9e4;
    --ink: #3f3f3f;
    --purple: #a3238a;
    --purple-dark: #7d1a68;
    --orange: #e5582a;
    --orange-light: #ec8763;
    --orange-dark: #c1492a;
    --white: #ffffff;
  }
  * { margin: 0; padding: 0; box-sizing: border-box; }
  html, body {
    width: 1200px;
    height: 887px;
    overflow: hidden;
    background: var(--stage);
    font-family: "Ubuntu", sans-serif;
  }
  .poster {
    position: absolute;
    left: 300px;
    top: 20px;
    width: 600px;
    height: 846px;
    background: var(--paper);
    box-shadow: 0 6px 18px rgba(0,0,0,0.25);
    overflow: hidden;
  }
  .poster-art {
    position: absolute;
    inset: 0;
    width: 600px;
    height: 846px;
  }
  .sanitiser-pitch {
    position: absolute;
    left: 18px;
    top: 400px;
    width: 230px;
    text-align: center;
    color: var(--ink);
    font-size: 25px;
    font-weight: 500;
    line-height: 47px;
  }
  .sanitiser-pitch .stat {
    color: var(--orange);
    font-size: 30px;
    font-weight: 700;
  }
  .call-to-action {
    position: absolute;
    left: 260px;
    top: 400px;
    width: 328px;
    text-align: center;
    color: var(--white);
    font-weight: 500;
    text-shadow: 0 1px 2px rgba(0,0,0,0.15);
  }
  .call-to-action .line-try { display: block; font-size: 37px; line-height: 46px; }
  .call-to-action .line-free { display: block; font-size: 54px; line-height: 70px; margin-top: 4px; }
  .advertise-invite {
    position: absolute;
    left: 0;
    top: 682px;
    width: 600px;
    text-align: center;
    color: var(--ink);
    font-size: 21px;
  }
  .brand-mark {
    position: absolute;
    left: 0;
    top: 748px;
    width: 600px;
    display: flex;
    justify-content: center;
    align-items: center;
    gap: 10px;
  }
  .brand-mark .dot {
    width: 30px;
    height: 30px;
    border-radius: 50%;
    background: var(--purple);
  }
  .brand-mark .name {
    color: var(--purple);
    font-size: 26px;
    font-weight: 500;
  }
  .contact-bar {
    position: absolute;
    left: 0;
    bottom: 0;
    width: 600px;
    height: 34px;
    display: flex;
    color: var(--white);
    font-size: 19px;
    font-weight: 500;
  }
  .contact-bar span {
    flex: 1;
    display: flex;
    align-items: center;
    justify-content: center;
  }
</style>
</head>
<body>
  <main class="poster">
    <svg class="poster-art" viewBox="0 0 488 688" preserveAspectRatio="none" aria-hidden="false">
      <defs>
        <linearGradient id="hands-tone" x1="0" y1="0" x2="1" y2="1">
          <stop offset="0" stop-color="#b27a57"/>
          <stop offset="0.45" stop-color="#e9dcd2"/>
          <stop offset="1" stop-color="#f6f5f2"/>
        </linearGradient>
        <linearGradient id="arrow-fill" x1="0" y1="0" x2="0" y2="1">
          <stop offset="0" stop-color="var(--orange-light)"/>
          <stop offset="1" stop-color="var(--orange-dark)"/>
        </linearGradient>
        <linearGradient id="bar-fill" x1="0" y1="0" x2="0" y2="1">
          <stop offset="0" stop-color="var(--purple)"/>
          <stop offset="1" stop-color="var(--purple-dark)"/>
        </linearGradient>
      </defs>

      <!-- hero photo area -->
      <rect class="hero-photo" x="0" y="0" width="330" height="280" fill="url(#hands-tone)"
            role="img" aria-label="Photo of two cupped hands covered in soap lather"/>
      <path class="hero-curve-mask" d="M0 280 L330 280 L330 300 L0 300 Z" fill="var(--paper)"/>
      <path class="hero-curve" d="M0 294 C150 292 300 250 488 40" fill="none" stroke="var(--purple)" stroke-width="4"/>

      <!-- message band -->
      <rect class="message-band" x="0" y="308" width="488" height="220" fill="var(--band)"/>
      <line x1="0" y1="308" x2="488" y2="308" stroke="#d6d4ce" stroke-width="1"/>
      <line x1="0" y1="528" x2="488" y2="528" stroke="#d6d4ce" stroke-width="1"/>

      <!-- arrow call-to-action -->
      <path class="cta-arrow" d="M211 310 H478 V470 L344 503 L211 470 Z" fill="url(#arrow-fill)"/>

      <!-- germ burst -->
      <polygon class="germ-burst"
        points="365,128 381,178 420,150 410,196 460,198 418,222 458,250 410,254 425,300 384,276 370,318 352,278 316,302 326,258 276,250 318,226 275,198 324,194 314,150 352,176"
        fill="var(--white)" stroke="var(--purple)" stroke-width="3" stroke-linejoin="round"/>
      <circle class="germ-character" cx="365" cy="225" r="34" fill="#e4581e"
              role="img" aria-label="Friendly orange cartoon germ character"/>

      <!-- contact bar -->
      <rect class="contact-bar-bg" x="0" y="661" width="488" height="27" fill="url(#bar-fill)"/>
      <line x1="245" y1="663" x2="245" y2="686" stroke="rgba(255,255,255,0.35)" stroke-width="1"/>
    </svg>

    <p class="sanitiser-pitch">
      Use our<br>complimentary<br>sanitiser which<br>is effective on<br><span class="stat">99.9%</span> of germs
    </p>

    <h1 class="call-to-action">
      <span class="line-try">Try it NOW!</span>
      <span class="line-free">It’s FREE!</span>
    </h1>

    <p class="advertise-invite">Use This Space To Advertise:</p>

    <div class="brand-mark">
      <span class="dot"></span>
      <span class="name">Brelvona</span>
    </div>

    <footer class="contact-bar">
      <span class="web">Brelvona.com.au</span>
      <span class="email">info@brelvona.com.au</span>
    </footer>
  </main>
</body>
</html>
```